TORNWICK Pizza Flyer / Menu

Hello so its a new pizza shop called Tornwick. I need a flyer menu designed . it will be 30cm tall and 10.5cm wide. i made one which i have uploaded but as you can see im not very skillfull design wise. I did want the logo on the front with the photo of the counter in the middle and then half the pizza at the bottom. then on the back i wanted all the different toppings ( doesnt have to be the same pics as i have used ) and then drinks and desserts underneath and our contact details. I dont want to include our signature specials. Also facebook/twitter and instagram logos somewhere. the font i have been using is called 'AR CENA' i have attached a rough sketch i have put together to give you an idea too. thanks

Industry/Entity Type

Shop

```html
<!DOCTYPE html>
<html lang="en">
<head>
<meta charset="utf-8">
<title>Tornwick Pizza Flyer</title>
<link href="https://fonts.googleapis.com/css2?family=Chewy&display=swap" rel="stylesheet">
<style>
:root{
  --page:#d6d6d6;
  --dark:#1e0d0b;
  --maroon:#4a1410;
  --red:#7a1d16;
  --orange:#f29111;
  --white:#ffffff;
}
*{margin:0;padding:0;box-sizing:border-box}
html,body{width:873px;height:1200px;overflow:hidden;background:var(--page)}
body{position:relative;font-family:"Chewy","Trebuchet MS",cursive;color:var(--white)}
.panel{position:absolute;top:46px;width:385px;height:1100px;overflow:hidden;background:var(--dark)}
.panel--front{left:35px}
.panel--back{left:448px}
.backdrop{position:absolute;inset:0;background:radial-gradient(ellipse at 50% 50%,var(--red) 0%,var(--maroon) 45%,var(--dark) 100%)}
.abs{position:absolute}
.brand-dot{left:124px;top:44px;width:132px;height:132px;border-radius:50%;background:var(--orange)}
.front-name{left:0;width:100%;top:182px;text-align:center;font-size:48px;letter-spacing:3px;white-space:nowrap}
.photo{background:linear-gradient(160deg,#d9d2c6,#a59886 45%,#6e5a44)}
.photo--counter{left:0;top:340px;width:100%;height:262px}
.photo--pizza{left:0;top:900px;width:100%;height:200px;background:linear-gradient(160deg,#3a2a1e,#c98a3a 50%,#8a3a1e)}
.arc{left:0;width:100%;pointer-events:none}

/* text followed by a brush bar, never overlapping */
.bar-row{position:absolute;display:flex;align-items:center;gap:12px;white-space:nowrap}
.stroke{flex:1 1 auto;min-width:30px;height:12px;border-radius:6px 2px 8px 3px;background:var(--orange)}
.slogan-row{right:30px;font-size:46px;line-height:1}
.slogan-row .stroke{max-width:150px;margin-top:6px}
.heading-row{left:14px;right:25px;font-size:25px;letter-spacing:1px;line-height:1}
.heading-row .stroke{height:10px;max-width:190px;margin-top:4px}

.header-frame{left:32px;top:17px;width:320px;height:116px;border:3px solid var(--white);border-bottom:none}
.header-frame::after{content:"";position:absolute;left:-3px;right:-3px;bottom:0;height:3px;background:linear-gradient(90deg,var(--white) 8%,transparent 8%,transparent 92%,var(--white) 92%)}
.tagline{left:34px;top:40px;font-size:8px;letter-spacing:1px}
.brand-row{left:40px;right:40px;top:58px;display:flex;align-items:center;gap:10px;white-space:nowrap}
.mini-dot{flex:0 0 46px;height:46px;border-radius:50%;background:var(--orange)}
.back-name{font-size:38px;letter-spacing:3px;line-height:1}
.est{right:42px;top:106px;font-size:10px}
.address{left:0;width:100%;top:138px;text-align:center;font-size:10px;letter-spacing:.5px;white-space:nowrap}
.price-badge{flex:0 0 52px;height:30px;border-radius:50%;background:var(--orange);border:2px solid var(--white);text-align:center;font-size:15px;line-height:26px}
.heading-row--build .stroke{max-width:none}

.toppings{left:10px;top:214px;width:365px;display:grid;grid-template-columns:repeat(7,52px);grid-auto-rows:70px}
.topping{display:flex;flex-direction:column;align-items:center}
.topping__img{flex:0 0 45px;width:45px;border-radius:50%;border:2px solid var(--orange)}
.topping__name{margin-top:3px;width:50px;font-size:7px;line-height:8px;text-align:center;overflow-wrap:break-word}

.price-list{left:22px;width:335px;list-style:none;font-size:15px;letter-spacing:.5px}
.price-list li{display:flex;justify-content:space-between;height:25.5px;white-space:nowrap}
.info{left:0;width:100%;text-align:center;font-size:12px;letter-spacing:.3px;white-space:nowrap}
.phone{left:0;width:100%;text-align:center;top:906px;font-size:34px;color:var(--orange);letter-spacing:2px;white-space:nowrap}
.social{top:1024px;width:36px;height:36px;border-radius:5px;background:var(--white);border:3px solid #9aa5b5}
.corner-dot{left:-70px;top:990px;width:160px;height:160px;border-radius:50%;background:var(--orange)}
</style>
</head>
<body>

<section class="panel panel--front">
  <div class="backdrop" role="img" aria-label="Dark red ornamental swirl pattern background"></div>
  <div class="abs brand-dot"></div>
  <div class="abs front-name">TORNWICK</div>

  <div class="abs photo photo--counter" role="img" aria-label="Photo of the topping counter with trays of fresh ingredients"></div>
  <svg class="abs arc" style="top:326px" width="385" height="40" viewBox="0 0 385 40"><path d="M0 40 Q190 -10 385 22 L385 8 Q190 -22 0 24 Z" fill="var(--orange)"/></svg>
  <svg class="abs arc" style="top:582px" width="385" height="46" viewBox="0 0 385 46"><path d="M0 44 Q190 2 385 30 L385 18 Q190 -10 0 30 Z" fill="var(--orange)"/></svg>

  <div class="bar-row slogan-row" style="left:52px;top:636px"><span>QUICK</span><span class="stroke"></span></div>
  <div class="bar-row slogan-row" style="left:24px;top:698px"><span>CUSTOM</span><span class="stroke"></span></div>
  <div class="bar-row slogan-row" style="left:66px;top:760px"><span>PIZZA</span><span class="stroke"></span></div>

  <div class="abs photo photo--pizza" role="img" aria-label="Photo of pizza slices with fresh toppings"></div>
  <svg class="abs arc" style="top:880px" width="385" height="40" viewBox="0 0 385 40"><path d="M0 34 Q190 -6 385 26 L385 12 Q190 -18 0 20 Z" fill="var(--orange)"/></svg>
</section>

<section class="panel panel--back">
  <div class="backdrop" role="img" aria-label="Dark red ornamental swirl pattern background"></div>

  <div class="abs header-frame"></div>
  <div class="abs tagline">DESIGNER PIZZA</div>
  <div class="abs brand-row"><span class="mini-dot"></span><span class="back-name">TORNWICK</span></div>
  <div class="abs est">EST2016</div>
  <div class="abs address">12 MILL YARD, ASHCOMBE, KENFIELD, KF4 2RD</div>

  <div class="bar-row heading-row heading-row--build" style="top:180px;left:20px"><span>BUILD IT!...</span><span class="stroke"></span><span class="price-badge">6.99</span></div>

  <div class="abs toppings">
    <div class="topping"><div class="topping__img" style="background:#f2c21b" role="img" aria-label="Pineapple"></div><span class="topping__name">PINEAPPLE</span></div>
    <div class="topping"><div class="topping__img" style="background:#d9492a" role="img" aria-label="Pepperoni"></div><span class="topping__name">PEPPERONI</span></div>
    <div class="topping"><div class="topping__img" style="background:#c81d1d" role="img" aria-label="Red pepper"></div><span class="topping__name">RED PEPPER</span></div>
    <div class="topping"><div class="topping__img" style="background:#1c1c1c" role="img" aria-label="Black olive"></div><span class="topping__name">BLACK OLIVE</span></div>
    <div class="topping"><div class="topping__img" style="background:#3f8a2a" role="img" aria-label="Spinach"></div><span class="topping__name">SPINACH</span></div>
    <div class="topping"><div class="topping__img" style="background:#efe6d6" role="img" aria-label="Garlic"></div><span class="topping__name">GARLIC</span></div>
    <div class="topping"><div class="topping__img" style="background:#f6f4ee" role="img" aria-label="Mozzarella"></div><span class="topping__name">MOZARELLA</span></div>

    <div class="topping"><div class="topping__img" style="background:#f1efe8" role="img" aria-label="Ricotta"></div><span class="topping__name">RICOTTA</span></div>
    <div class="topping"><div class="topping__img" style="background:#8ca62a" role="img" aria-label="Green olive"></div><span class="topping__name">GREENN OLIVE</span></div>
    <div class="topping"><div class="topping__img" style="background:#4ba02c" role="img" aria-label="Green pepper"></div><span class="topping__name">GREEN PEPPER</span></div>
    <div class="topping"><div class="topping__img" style="background:#b85a9a" role="img" aria-label="Onion"></div><span class="topping__name">ONION</span></div>
    <div class="topping"><div class="topping__img" style="background:#f0a424" role="img" aria-label="Cheddar cheese"></div><span class="topping__name">CHEDDAR CHEESE</span></div>
    <div class="topping"><div class="topping__img" style="background:#2f7a2a" role="img" aria-label="Basil"></div><span class="topping__name">BASIL</span></div>
    <div class="topping"><div class="topping__img" style="background:#c98a4a" role="img" aria-label="Pulled chicken"></div><span class="topping__name">PULLED CHICKEN</span></div>

    <div class="topping"><div class="topping__img" style="background:#6a3f24" role="img" aria-label="Pulled beef"></div><span class="topping__name">PULLED BEEF</span></div>
    <div class="topping"><div class="topping__img" style="background:#e6dccb" role="img" aria-label="Mushroom"></div><span class="topping__name">MUSHROOM</span></div>
    <div class="topping"><div class="topping__img" style="background:#d8281e" role="img" aria-label="Tomato"></div><span class="topping__name">TOMATO</span></div>
    <div class="topping"><div class="topping__img" style="background:#b83a3a" role="img" aria-label="Salami"></div><span class="topping__name">SALAMI</span></div>
    <div class="topping"><div class="topping__img" style="background:#6f7d2a" role="img" aria-label="Capers"></div><span class="topping__name">CAPERS</span></div>
    <div class="topping"><div class="topping__img" style="background:#3b8a24" role="img" aria-label="Jalapenos"></div><span class="topping__name">JALAPENOS</span></div>
    <div class="topping"><div class="topping__img" style="background:#b26a52" role="img" aria-label="Anchovies"></div><span class="topping__name">ANCHOVIES</span></div>

    <div class="topping"><div class="topping__img" style="background:#f3c51a" role="img" aria-label="Corn"></div><span class="topping__name">CORN</span></div>
    <div class="topping"><div class="topping__img" style="background:#c2161a" role="img" aria-label="Chilli"></div><span class="topping__name">CHILLI</span></div>
    <div class="topping"><div class="topping__img" style="background:#4a1a10" role="img" aria-label="BBQ sauce"></div><span class="topping__name">B-B-Q</span></div>
    <div class="topping"><div class="topping__img" style="background:#4f8a1e" role="img" aria-label="Pesto"></div><span class="topping__name">PESTO</span></div>
    <div class="topping"><div class="topping__img" style="background:#8a2a22" role="img" aria-label="Chorizo"></div><span class="topping__name">CHORIZO</span></div>
    <div class="topping"><div class="topping__img" style="background:#efd79a" role="img" aria-label="Parmesan"></div><span class="topping__name">PARMESAN</span></div>
    <div class="topping"><div class="topping__img" style="background:#e2461e" role="img" aria-label="Sweet chilli sauce"></div><span class="topping__name">SWEET CHILLI</span></div>
  </div>

  <div class="bar-row heading-row" style="top:522px"><span>DESSERTS...</span><span class="stroke"></span></div>
  <ul class="abs price-list" style="top:570px">
    <li><span>BANANAHAZEL PIZZA!!!</span><span>3.99</span></li>
    <li><span>CREME BRULEE</span><span>2.49</span></li>
    <li><span>TIRAMISU</span><span>2.49</span></li>
    <li><span>CHOCO DREAMCAKE</span><span>2.49</span></li>
  </ul>

  <div class="bar-row heading-row" style="top:712px"><span>DRINKS...</span><span class="stroke"></span></div>
  <ul class="abs price-list" style="top:760px">
    <li><span>BLOOD ORANGE</span><span>0.99</span></li>
    <li><span>ORENGEADE</span><span>0.99</span></li>
    <li><span>LEMON</span><span>0.99</span></li>
    <li><span>FIZZ COLA</span><span>0.89</span></li>
  </ul>

  <div class="abs info" style="top:866px;font-size:11.5px">WOOD STONE PIZZA DELIVERY HOT TO YOUR DOOR STEP</div>
  <div class="abs info" style="top:886px;font-size:11px">MINIMUN ORDER 12£</div>
  <div class="abs phone">0207 555 0192</div>
  <div class="abs info" style="top:958px">FOLLOW FOR UPDATES, OFFERS AND IF YOUR LUCKY...</div>
  <div class="abs info" style="top:976px">A FREE PIZZA</div>

  <div class="abs social" style="left:142px"></div>
  <div class="abs social" style="left:186px"></div>
  <div class="abs social" style="left:230px"></div>

  <div class="abs corner-dot"></div>
</section>

</body>
</html>
```